New Electrical Business advertisement

We Need an A4 flyer created advertising we are a new electrical company servicing this area. We need the flyer to stand out and have a friendly feel to it

Target Market(s)

Home owners and commerical business

Industry/Entity Type

Electrician

Font styles to use
Sans Serif

Requirements
Must have
• must stand out, be eye catching but have a professional feel

Must have company colours orange and blue
RBG Colours
BLUE: R:4 G:116 B:187
ORANGE: R:240 G:86 B:47

```html
<!DOCTYPE html>
<html lang="en">
<head>
<meta charset="utf-8">
<title>Ridgeline Electrical – Flyer</title>
<link href="https://fonts.googleapis.com/css2?family=Montserrat:wght@400;500;700&family=Open+Sans:wght@400&display=swap" rel="stylesheet">
<style>
  :root{
    --blue:#0474bb;
    --orange:#f0562f;
    --white:#ffffff;
    --ink:#1d1d1d;
    --photo-a:#c9c2b4;
    --photo-b:#8e8f93;
    --photo-c:#a8b6c6;
  }
  html,body{margin:0;padding:0;overflow:hidden;background:#ffffff;}
  .flyer{position:relative;width:848px;height:1200px;overflow:hidden;background:var(--white);font-family:"Montserrat",sans-serif;}
  .hero-photo{position:absolute;left:0;top:0;width:848px;height:610px;
    background:
      linear-gradient(180deg,rgba(40,40,45,0) 70%,rgba(40,40,45,.55) 100%),
      linear-gradient(110deg,var(--photo-c) 0%,var(--photo-a) 45%,var(--photo-b) 100%);}
  .shapes{position:absolute;left:0;top:0;}
  .hero-tagline{position:absolute;left:16px;top:490px;width:260px;text-align:center;color:var(--white);
    font-weight:500;font-size:20px;line-height:27px;letter-spacing:.2px;margin:0;white-space:nowrap;}
  .brand-top{position:absolute;left:585px;top:58px;display:flex;align-items:center;gap:8px;}
  .brand-dot{width:12px;height:12px;border-radius:50%;background:var(--orange);}
  .brand-name{font-weight:700;font-size:15px;color:var(--blue);letter-spacing:.3px;}
  .about{position:absolute;left:56px;top:622px;width:422px;}
  .about h2{margin:0;font-weight:700;font-size:26px;line-height:35px;letter-spacing:.5px;}
  .about .h-orange{color:var(--orange);}
  .about .h-blue{color:var(--blue);margin-top:22px;}
  .about p{margin:4px 0 0;font-family:"Open Sans",sans-serif;font-size:11.2px;line-height:15.5px;color:var(--ink);text-align:justify;}
  .about p + p{margin-top:15px;}
  .contact-bar{position:absolute;left:14px;top:1129px;width:491px;height:55px;background:var(--blue);color:var(--white);
    font-size:12.3px;box-sizing:border-box;padding:9px 18px 0;}
  .contact-row{display:flex;justify-content:space-between;}
  .contact-address{text-align:center;margin-top:6px;}
  .services{position:absolute;left:566px;top:608px;width:270px;color:var(--white);}
  .services h2{margin:0;font-weight:700;font-size:26px;line-height:35px;letter-spacing:.5px;}
  .service-list{list-style:none;margin:22px 0 0;padding:0;}
  .service-item{display:flex;align-items:center;height:75px;}
  .service-icon{width:44px;height:44px;flex:none;margin-right:36px;}
  .service-label{font-size:20.5px;line-height:30px;font-weight:400;letter-spacing:.3px;}
  .brand-bottom{position:absolute;left:515px;top:1138px;width:333px;display:flex;justify-content:center;align-items:center;gap:8px;}
  .brand-bottom .brand-dot{background:var(--white);}
  .brand-bottom .brand-name{color:var(--white);font-size:19px;}
</style>
</head>
<body>
<div class="flyer">
  <div class="hero-photo" role="img" aria-label="Photo of an electrician in a hard hat testing wiring in a switchboard"></div>

  <svg class="shapes" width="848" height="1200" viewBox="0 0 848 1200" aria-hidden="true">
    <path d="M519,0 L848,0 L848,104 L632,104 Q600,104 585,86 Z" fill="var(--white)"/>
    <path d="M0,566 Q110,600 366,538 Q620,470 848,522 L848,1200 L0,1200 Z" fill="var(--white)"/>
    <path d="M366,538 Q620,455 848,512 L848,602 Q720,540 515,538 Z" fill="var(--blue)"/>
    <path d="M515,538 Q720,540 848,602 L848,1200 L515,1200 Z" fill="var(--orange)"/>
  </svg>

  <p class="hero-tagline">FOR ALL YOUR<br>ELECTRICAL NEEDS</p>

  <div class="brand-top"><span class="brand-dot"></span><span class="brand-name">RIDGELINE ELECTRICAL</span></div>

  <section class="about">
    <h2 class="h-orange">RIDGELINE<br>ELECTRICAL IS A</h2>
    <p>Lorem ipsum dolor sit amet, consectetuer adipiscing elit, sed diam nonummy nibh euismod tincidunt ut laoreet dolore magna aliquam erat volutpat. Ut wisi enim ad minim veniam, quis nostrud exerci tation ullamcorper suscipit lobortis nisl ut aliquip ex ea commodo consequat. Duis autem vel eum iriure dolor in hendrerit in vulputate velit esse molestie consequat, vel illum dolore eu feugiat nulla facilisis at vero eros et accumsan et iusto odio dignissim qui blandit praesent luptatum zzril delenit augue duis dolore te feugait nulla facilisi.</p>
    <h2 class="h-blue">OUR<br>PHILOSOPHY</h2>
    <p>Lorem ipsum dolor sit amet, consectetuer adipiscing elit, sed diam nonummy nibh euismod tincidunt ut laoreet dolore magna aliquam erat volutpat. Ut wisi enim ad minim veniam, quis nostrud exerci tation ullamcorper suscipit lobortis nisl ut aliquip ex ea commodo consequat. Duis autem vel eum iriure dolor in hendrerit in vulputate velit esse molestie consequat, vel illum dolore eu feugiat nulla facilisis at vero eros et accumsan et iusto odio dignissim qui blandit praesent luptatum zzril delenit augue duis dolore te feugait nulla facilisi.</p>
    <p>Lorem ipsum dolor sit amet, consectetuer adipiscing elit, sed diam nonummy nibh euismod tincidunt ut laoreet dolore magna aliquam erat volutpat. Ut wisi enim ad minim veniam, quis nostrud exerci tation ullamcorper suscipit lobortis nisl ut aliquip</p>
  </section>

  <div class="contact-bar">
    <div class="contact-row"><span>555-014-2290</span><span>hello@ridgelinepower.com</span><span>www.ridgelinepower.com</span></div>
    <div class="contact-address">118 Harbor View Road, Easton, MA 02375</div>
  </div>

  <section class="services">
    <h2>ELECTRICAL<br>SERVICES</h2>
    <ul class="service-list">
      <li class="service-item">
        <svg class="service-icon" viewBox="0 0 44 44" aria-hidden="true"><circle cx="22" cy="22" r="19" fill="none" stroke="var(--white)" stroke-width="4"/><path d="M25,10 L16,24 L22,24 L19,34 L28,20 L22,20 Z" fill="var(--white)"/></svg>
        <span class="service-label">New<br>Installations</span>
      </li>
      <li class="service-item">
        <svg class="service-icon" viewBox="0 0 44 44" aria-hidden="true"><circle cx="22" cy="22" r="19" fill="none" stroke="var(--white)" stroke-width="4"/><path d="M25,10 L16,24 L22,24 L19,34 L28,20 L22,20 Z" fill="var(--white)"/></svg>
        <span class="service-label">Renovations<br>and Re-Wiring</span>
      </li>
      <li class="service-item">
        <svg class="service-icon" viewBox="0 0 44 44" aria-hidden="true"><circle cx="22" cy="22" r="19" fill="none" stroke="var(--white)" stroke-width="4"/><path d="M25,10 L16,24 L22,24 L19,34 L28,20 L22,20 Z" fill="var(--white)"/></svg>
        <span class="service-label">Installation and<br>Safety Switches</span>
      </li>
      <li class="service-item">
        <svg class="service-icon" viewBox="0 0 44 44" aria-hidden="true"><circle cx="22" cy="22" r="19" fill="none" stroke="var(--white)" stroke-width="4"/><path d="M25,10 L16,24 L22,24 L19,34 L28,20 L22,20 Z" fill="var(--white)"/></svg>
        <span class="service-label">Switchboard<br>upgrades</span>
      </li>
      <li class="service-item">
        <svg class="service-icon" viewBox="0 0 44 44" aria-hidden="true"><circle cx="22" cy="22" r="19" fill="none" stroke="var(--white)" stroke-width="4"/><path d="M25,10 L16,24 L22,24 L19,34 L28,20 L22,20 Z" fill="var(--white)"/></svg>
        <span class="service-label">Services and<br>breakdowns</span>
      </li>
    </ul>
  </section>

  <div class="brand-bottom"><span class="brand-dot"></span><span class="brand-name">RIDGELINE ELECTRICAL</span></div>
</div>
</body>
</html>
```